依頼概要
■依頼の目的/概要
・電子書籍(自己啓発系)の表紙デザインをお願いします。
・電子書籍は、ソルベリアで販売します。pagoraです。

■本の内容
・初出版本です。
・行き詰った人生を何とかしたいなら、人間関係の苦しみを解消したいなら…。自分の『あり方』を変えることによって、人生がうまくいく方向に動きだすよ ということをお伝えする内容になっています。
・作者の経験が、本の元になっています。
・働く世代や、実際に苦しんでいる当事者、ひきこもりの子どもを持つ親など、幅広く読んでもらいたいです。

■デザイン要望
・明るい未来を感じられるような表紙デザインにしてください。
(底抜けに明るいのは×だけど、悲壮感が見えるのも×)
・人物や、絵が入っている表紙が望ましいです。
(イラスト・写真〇。文字のみのデザインは、×)

■本のタイトル
・本のタイトルは、

毎日が「疲れた…」と感じる君へ、ひとつずつ笑顔が戻ってくる、小さな灯火の地図

です。

・サブキャッチに

~胸のざわめきの理由は〝本音の迷子〟だった~

を入れてください。

■ごあいさつ
・その他、ご不明な点がありましたらお気軽にご質問ください。よろしくお願いします。

■ 選んだ理由

Talkvineをつかって、皆さんからいただいた仮案をアンケートさせていただいたところ、
もっとも「いい」「好き」という評価をいただけたのが、今回選ばせていただいたデザインでした。

なぜよかったのか? と聞いてみたところ
「右下のキャラクターが可愛い」
「見ていると、癒される」
「澄ちゃん(私のこと)らしい」
という意見が、出そろいました。

正直に申しますと、私自身も意外だったのですが
多くの人から「このデザインがいちばん私らしい」と言っていただけるので、気になりはじめ、
今では私自身も気に入っております。

■ 提案者全員のお礼・コメント

本当にありがとうございました。

たった一つのデザインを決めるために、たくさんの方から頂いたデザインを落とさなければならないため、胸を痛めました。
落とすには、あまりにも私好みのデザインがあり過ぎました。

中には私の、初出版の、あまり上手とはいえない文章を丁寧に読んでくれる方もいらっしゃり、とても嬉しかったです。
ありがとうございます。
感謝しています。

また何かの折、お世話になることがあれば、よろしくお願いいたします。

```html
<!DOCTYPE html>
<html lang="ja">
<head>
<meta charset="utf-8">
<title>小さな灯火の地図 — 表紙</title>
<link rel="stylesheet" href="https://fonts.googleapis.com/css2?family=Noto+Sans+JP:wght@500;700;900&display=swap">
<style>
  :root {
    --night: #041a2a;
    --deep-teal: #06384a;
    --glow-teal: #1a8fa0;
    --stage-blue: #0c3a5c;
    --banner: #f4f8fb;
    --ink: #0a0a0a;
    --gold: #f3e43a;
    --white: #ffffff;
    --pale: #d9eef2;
    --author: #5fb6d8;
  }
  html, body {
    margin: 0;
    padding: 0;
    overflow: hidden;
    background: var(--night);
  }
  .cover {
    position: relative;
    width: 750px;
    height: 1200px;
    overflow: hidden;
    font-family: "Noto Sans JP", sans-serif;
    background:
      radial-gradient(ellipse 70% 30% at 50% 72%, rgba(26,143,160,0.55), transparent 70%),
      linear-gradient(180deg, var(--night) 0%, var(--deep-teal) 60%, #0a4f5f 80%, var(--night) 100%);
  }
  .stage-photo {
    position: absolute;
    left: 0; top: 0;
    width: 750px; height: 620px;
    background:
      radial-gradient(ellipse 40% 60% at 20% 30%, rgba(120,200,230,0.35), transparent 70%),
      radial-gradient(ellipse 25% 35% at 12% 55%, rgba(170,40,60,0.45), transparent 70%),
      linear-gradient(180deg, #0a2c44 0%, var(--stage-blue) 55%, rgba(6,56,74,0) 100%);
  }
  .banner {
    position: absolute;
    left: 0; top: 0;
    width: 750px; height: 460px;
  }
  .catch {
    position: absolute;
    left: 0; top: 0;
    width: 750px; height: 460px;
    color: var(--ink);
    font-weight: 900;
  }
  .catch span { position: absolute; white-space: nowrap; line-height: 1; }
  .catch-line1 { left: 420px; top: 70px; font-size: 46px; }
  .catch-big { left: 262px; top: 140px; font-size: 64px; letter-spacing: -2px; }
  .catch-after { left: 470px; top: 232px; font-size: 44px; }
  .catch-line3 { left: 300px; top: 300px; font-size: 44px; }
  .promise {
    position: absolute;
    left: 0; top: 620px;
    width: 750px; height: 110px;
    color: var(--gold);
    font-weight: 700;
    text-shadow: 0 0 10px rgba(0,0,0,0.5);
  }
  .promise span { position: absolute; line-height: 1; }
  .promise .small { font-size: 52px; }
  .promise .big { font-size: 66px; }
  .title {
    position: absolute;
    left: 0; top: 735px;
    width: 750px;
    margin: 0;
    text-align: center;
    font-size: 84px;
    font-weight: 900;
    color: var(--white);
    letter-spacing: 2px;
    line-height: 1.1;
    text-shadow: 0 0 6px var(--glow-teal), 0 0 18px var(--glow-teal), 0 4px 6px rgba(0,0,0,0.6);
  }
  .title-tail {
    position: absolute;
    left: 0; top: 860px;
    width: 750px;
    text-align: center;
    font-size: 52px;
    font-weight: 700;
    color: var(--gold);
    letter-spacing: 26px;
    line-height: 1;
  }
  .subtitle {
    position: absolute;
    left: 0; top: 948px;
    width: 750px;
    margin: 0;
    text-align: center;
    font-size: 28px;
    font-weight: 500;
    color: var(--pale);
    line-height: 1;
  }
  .author {
    position: absolute;
    left: 10px; top: 1160px;
    margin: 0;
    font-size: 26px;
    font-weight: 700;
    color: var(--author);
    line-height: 1;
  }
</style>
</head>
<body>
<div class="cover">
  <div class="stage-photo" role="img" aria-label="スポットライトを浴びた舞台で両手を広げる赤いコートの人物と赤い椅子の写真"></div>

  <svg class="banner" viewBox="0 0 750 460" aria-hidden="true">
    <path d="M232 60 C300 20 380 50 460 30 C540 10 610 40 690 18
             C660 90 700 160 670 230 C650 280 700 330 690 360
             C640 340 600 370 560 360 C530 390 515 420 505 450
             C490 410 470 380 430 370 C370 360 320 390 270 370
             C250 370 245 385 238 380 C260 300 220 230 240 160
             C250 120 225 90 232 60 Z"
          fill="var(--banner)" opacity="0.95"/>
  </svg>

  <div class="catch">
    <span class="catch-line1">毎日が</span>
    <span class="catch-big">「疲れた…」</span>
    <span class="catch-after">と感じる</span>
    <span class="catch-line3">君へ</span>
  </div>

  <div class="promise">
    <span class="small" style="left:40px; top:10px;">ひ</span>
    <span class="small" style="left:100px; top:50px;">と</span>
    <span class="small" style="left:160px; top:10px;">つ</span>
    <span class="small" style="left:220px; top:50px;">ず</span>
    <span class="small" style="left:280px; top:10px;">つ</span>
    <span class="big" style="left:360px; top:0px;">笑</span>
    <span class="big" style="left:460px; top:36px;">顔</span>
    <span class="small" style="left:620px; top:10px;">が</span>
  </div>

  <h1 class="title">小さな灯火の地図</h1>
  <div class="title-tail">戻ってくる</div>

  <p class="subtitle">~胸のざわめきの理由は〝本音の迷子〟だった~</p>

  <p class="author">秋津澄人著</p>
</div>
</body>
</html>
```